Business Card and Stationary Designs for commercial construction company
Halvern Builders, Inc.
Creative Brief
Use standard fonts
Dennis Whitlock
Director of Operations
6387 Larkmeadow Lane Elk Grove, CA 95731
dennis.whitlock@halvernbldg.com
License #3084519
We like the colors of our logo, so please incorporate them into the card. The font for the other information on the business card does not have to match the logo font, but it should coordinate with it. We need the stationary design to be used to print actual stationary, but we would also like a word document that we can use for creating letters on electronic stationary.

```html
<!DOCTYPE html>
<html lang="en">
<head>
<meta charset="utf-8">
<title>Halvern Builders, Inc. — Business Card</title>
<link href="https://fonts.googleapis.com/css2?family=Montserrat:wght@700&family=Open+Sans:wght@400;600&display=swap" rel="stylesheet">
<style>
  :root {
    --backdrop: #e9e7e4;
    --card: #ffffff;
    --brand-red: #d7262e;
    --brand-grey: #6d6e70;
    --text-dark: #4a4a4c;
    --text-soft: #7b7b7d;
    --rule: #c9c9cb;
    --swoosh-grey: #bfc0c2;
  }
  * { margin: 0; padding: 0; box-sizing: border-box; }
  html, body { width: 1200px; height: 901px; overflow: hidden; }
  body {
    background: var(--backdrop);
    display: flex; align-items: center; justify-content: center;
    font-family: "Open Sans", Arial, sans-serif;
  }
  .business-card {
    position: relative;
    width: 900px; height: 514px;
    background: var(--card);
    border-radius: 34px;
    overflow: hidden;
    box-shadow: 0 14px 40px rgba(0,0,0,.16);
  }
  .card-swoosh { position: absolute; left: 0; top: 0; }
  .brand-lockup {
    position: absolute; left: 120px; top: 200px;
    display: flex; align-items: center; gap: 14px;
  }
  .brand-square { width: 34px; height: 34px; background: var(--brand-red); }
  .brand-name {
    font-family: "Montserrat", Arial, sans-serif;
    font-weight: 700; font-size: 44px; letter-spacing: 1px;
    color: var(--brand-grey);
  }
  .divider {
    position: absolute; left: 445px; top: 36px;
    width: 1px; height: 250px; background: var(--rule);
  }
  .contact-block { position: absolute; left: 468px; top: 36px; color: var(--text-dark); }
  .person-name {
    font-size: 22px; font-weight: 600; letter-spacing: 1.5px;
    text-transform: uppercase; color: var(--brand-red); line-height: 1.2;
  }
  .person-title { font-size: 15px; color: var(--text-soft); margin-top: 2px; }
  .address { font-size: 15px; line-height: 1.45; margin-top: 26px; }
  .contact-list { list-style: none; margin-top: 24px; font-size: 14px; }
  .contact-list li { display: flex; align-items: center; gap: 10px; height: 24px; }
  .contact-icon { width: 14px; height: 14px; flex: none; }
</style>
</head>
<body>
  <div class="business-card">
    <svg class="card-swoosh" width="900" height="514" viewBox="0 0 900 514" aria-hidden="true">
      <path d="M0 470 C 250 360, 560 330, 900 250 L900 514 L0 514 Z" fill="var(--swoosh-grey)"/>
      <path d="M0 450 C 250 345, 560 315, 900 235 L900 258 C 560 338, 250 372, 0 478 Z" fill="var(--brand-red)"/>
      <path d="M0 492 C 260 392, 560 360, 900 286 L900 514 L0 514 Z" fill="#f1f1f2"/>
    </svg>

    <div class="brand-lockup">
      <span class="brand-square"></span>
      <span class="brand-name">HALVERN</span>
    </div>

    <div class="divider"></div>

    <div class="contact-block">
      <p class="person-name">Dennis Whitlock</p>
      <p class="person-title">Director of Operations</p>
      <p class="address">6387 Larkmeadow Lane<br>Elk Grove, CA 95731</p>
      <ul class="contact-list">
        <li>
          <svg class="contact-icon" viewBox="0 0 14 14"><rect width="14" height="14" rx="2" fill="var(--brand-red)"/><path d="M4 3.5 L5.8 3.5 L6.4 5.6 L5.4 6.4 C5.9 7.5 6.6 8.2 7.6 8.6 L8.4 7.6 L10.5 8.2 L10.5 10 C7 10.3 3.7 7 4 3.5Z" fill="#fff"/></svg>
          916 555 0142
        </li>
        <li>
          <svg class="contact-icon" viewBox="0 0 14 14"><rect width="14" height="14" rx="2" fill="var(--brand-red)"/><rect x="4.5" y="2.8" width="5" height="8.4" rx="1" fill="#fff"/></svg>
          916 555 0187
        </li>
        <li>
          <svg class="contact-icon" viewBox="0 0 14 14"><rect width="14" height="14" rx="2" fill="var(--brand-red)"/><rect x="3" y="5" width="8" height="5" fill="#fff"/><rect x="4.5" y="2.5" width="5" height="3" fill="#fff"/></svg>
          916 555 0199
        </li>
        <li>
          <svg class="contact-icon" viewBox="0 0 14 14"><rect width="14" height="14" rx="2" fill="var(--brand-red)"/><rect x="3" y="4" width="8" height="6" fill="#fff"/><path d="M3 4 L7 7.5 L11 4" stroke="var(--brand-red)" stroke-width="1" fill="none"/></svg>
          dennis.whitlock@halvernbldg.com
        </li>
        <li>
          <svg class="contact-icon" viewBox="0 0 14 14"><rect width="14" height="14" rx="2" fill="var(--brand-red)"/><circle cx="7" cy="7" r="3.8" stroke="#fff" stroke-width="1.1" fill="none"/><path d="M3.2 7 H10.8 M7 3.2 C5.5 5 5.5 9 7 10.8 C8.5 9 8.5 5 7 3.2" stroke="#fff" stroke-width="0.9" fill="none"/></svg>
          www.halvernbldg.com
        </li>
      </ul>
    </div>
  </div>
</body>
</html>
```